Electrical panel service sticker w Bucket truck & Logo

We have a rather plain sticker we put on lighting panels to remind customers who to call for service. We want to redesign them with brushed aluminum background. We want a remake of the sticker with the outline of a bucket truck. You'll need to find or draw the outling of a bucket truck maybe with the boom up slightly as we will get these stickers die cut.

We want LOGO with Ph.# and Email.
Electrical * Lighting * Sign Service

Target Market(s)

Commercial property managers

Industry/Entity Type

Property Management

Requirements
Must have
• Bucket Truck Outline

```html
<!DOCTYPE html>
<html lang="en">
<head>
<meta charset="utf-8">
<title>Brightpole Services – Panel Service Sticker</title>
<link rel="stylesheet" href="https://fonts.googleapis.com/css2?family=Oswald:wght@700&family=Archivo+Black&family=Roboto+Condensed:wght@700&family=Montserrat:wght@500&display=swap">
<style>
  :root {
    --page: #ffffff;
    --navy: #17406a;
    --red: #e8434a;
    --ink: #0d0d0d;
    --sticker-edge: #ffffff;
    --alu-light: #f4f5f6;
    --alu-mid: #d3d6d9;
    --alu-dark: #b5b9bd;
    --art-light: #e7ecf2;
    --art-dark: #c5d0dc;
  }
  html, body {
    margin: 0;
    padding: 0;
    width: 1200px;
    height: 900px;
    overflow: hidden;
    background: var(--page);
  }
  .sticker { display: block; width: 1200px; height: 900px; }
  .brand-name { font-family: "Oswald", "Arial Narrow", sans-serif; font-weight: 700; fill: var(--red); }
  .brand-suffix { font-family: "Montserrat", Arial, sans-serif; font-weight: 500; fill: var(--navy); letter-spacing: 3px; }
  .phone { font-family: "Archivo Black", "Arial Black", sans-serif; fill: var(--ink); stroke: var(--sticker-edge); stroke-width: 8; paint-order: stroke; }
  .email { font-family: "Roboto Condensed", "Arial Narrow", sans-serif; font-weight: 700; fill: var(--navy); stroke: var(--sticker-edge); stroke-width: 6; paint-order: stroke; }
  .services { font-family: "Archivo Black", "Arial Black", sans-serif; fill: var(--ink); letter-spacing: 2px; }
  .rule { stroke: var(--navy); stroke-width: 3; }
</style>
</head>
<body>
<svg class="sticker" viewBox="0 0 1200 900" xmlns="http://www.w3.org/2000/svg">
  <defs>
    <linearGradient id="brushed-aluminum" x1="0" y1="0" x2="1" y2="1">
      <stop offset="0" stop-color="var(--alu-dark)"/>
      <stop offset="0.3" stop-color="var(--alu-light)"/>
      <stop offset="0.55" stop-color="var(--alu-mid)"/>
      <stop offset="0.8" stop-color="var(--alu-light)"/>
      <stop offset="1" stop-color="var(--alu-dark)"/>
    </linearGradient>
    <linearGradient id="truck-art-tone" x1="0" y1="0" x2="0" y2="1">
      <stop offset="0" stop-color="var(--art-light)"/>
      <stop offset="1" stop-color="var(--art-dark)"/>
    </linearGradient>
    <filter id="edge-shadow" x="-5%" y="-5%" width="110%" height="115%">
      <feDropShadow dx="0" dy="3" stdDeviation="4" flood-color="#000" flood-opacity="0.28"/>
    </filter>
  </defs>

  <!-- die-cut tab above the plate -->
  <path class="die-cut-tab" filter="url(#edge-shadow)" fill="var(--sticker-edge)"
        d="M348,410 L348,262 Q348,238 378,232 L392,160 Q398,130 430,124 L730,58 Q748,52 770,52 L850,52 Q880,54 876,96 L866,226 Q864,258 876,284 L876,410 Z"/>

  <!-- brushed aluminum plate -->
  <rect class="plate" x="63" y="388" width="1083" height="461" rx="32"
        fill="url(#brushed-aluminum)" stroke="var(--sticker-edge)" stroke-width="8" filter="url(#edge-shadow)"/>

  <!-- bucket truck artwork area -->
  <rect class="truck-art" role="img" aria-label="Outline illustration of a navy bucket truck with its boom raised"
        x="362" y="96" width="490" height="332" rx="16" fill="url(#truck-art-tone)"/>
  <line class="ground-line" x1="250" y1="436" x2="985" y2="436" stroke="var(--navy)" stroke-width="3"/>

  <!-- company name -->
  <text class="brand-name" x="608" y="533" text-anchor="middle" font-size="92" textLength="925" lengthAdjust="spacingAndGlyphs">BRIGHTPOLE SERVICES</text>
  <line class="rule" x1="150" y1="568" x2="372" y2="568"/>
  <text class="brand-suffix" x="605" y="580" text-anchor="middle" font-size="34" textLength="410" lengthAdjust="spacingAndGlyphs">INCORPORATED</text>
  <line class="rule" x1="838" y1="568" x2="1052" y2="568"/>

  <!-- contact -->
  <text class="phone" x="602" y="706" text-anchor="middle" font-size="128" textLength="985" lengthAdjust="spacingAndGlyphs">877-555-0148</text>
  <text class="email" x="602" y="775" text-anchor="middle" font-size="60" textLength="985" lengthAdjust="spacingAndGlyphs">SERVICE@BRIGHTPOLESERVICES.COM</text>
  <text class="services" x="608" y="812" text-anchor="middle" font-size="28" textLength="820" lengthAdjust="spacingAndGlyphs">ELECTRICAL • LIGHTING • SIGN SERVICE</text>
</svg>
</body>
</html>
```